Voltarey - Flyer design

Description -
Motorhome and Caravan EWOFs
Recreational Vehicles (such as caravans, motorhomes, RVs, Boats etc) and Relocatable buildings that can be connected to an electricity supply must be regularly checked for electrical safety. An EWOF needs to be issued every 4 years.
Pre-purchase house inspections
A pre-purchase electrical inspection prior to buying a home can be used to identify any dangerous and unsafe electrical parts of the installation that may be costly to repair once the property has been purchased. Giving you peace of mind when buying your new home.
High risk Electrical inspections
All Prescribed Electrical Work that falls under the High Risk category must be inspected by a Registered Electrical Inspector and have a Record of Inspection certificate issued.
Electric Vehicle Chargers
Any electrical vehicle charger that can be accessed by the public (ie in a non-domestic situation) must be periodically inspected and certified every 12 months.
General Electrical Services
Domestic and commercial - We do new builds, Renovations, Maintenance and more!
Dean Fowler - Electrician and Electrical Inspector
Ph - 0227839152
Dean@voltarey.co.nz
Auckland
------
I also want there to be a few symbols similar to the files I have attached.
The main areas that I am hoping to find work is with caravans/motohomes and EV car chargers so these symbols are quite important.
Thanks so much

```html
<!DOCTYPE html>
<html lang="en">
<head>
<meta charset="utf-8">
<title>Voltarey Flyer</title>
<link href="https://fonts.googleapis.com/css2?family=Baloo+2:wght@600;700&family=Hind:wght@400;500;600;700&display=swap" rel="stylesheet">
<style>
:root{
  --green:#56b148;
  --green-deep:#17703a;
  --navy:#22334a;
  --teal-dark:#173f38;
  --grey:#676767;
  --paper:#ffffff;
  --mist:#e2e3e5;
  --ink:#1d3a3a;
  --stage:#555555;
}
*{margin:0;padding:0;box-sizing:border-box}
html,body{width:1200px;height:1200px;overflow:hidden;background:var(--stage)}
body{font-family:"Hind",sans-serif;color:var(--ink)}
.flyer{position:absolute;left:190px;top:20px;width:820px;height:1160px;background:var(--paper);overflow:hidden}
.abs{position:absolute}
.header{left:0;top:0;width:820px;height:270px}
.brand{left:50px;top:22px;font-family:"Hind",sans-serif;font-weight:600;font-size:72px;color:#fff;line-height:1;letter-spacing:-1px}
.tagline{left:50px;top:100px;font-family:"Hind",sans-serif;font-weight:500;font-size:20px;color:#fff}
.portrait{left:561px;top:-24px;width:232px;height:232px;border-radius:50%;border:10px solid #1d6a3c;background:radial-gradient(circle at 60% 40%,#d8d4cc,#6f7478 55%,#2b3138);}
.dotline{border-top:2px dotted var(--teal-dark)}
.dot{width:9px;height:9px;border-radius:50%;background:var(--teal-dark)}
.pill-dark{background:var(--teal-dark);color:#fff;border-radius:16px;text-align:center}
.section-pill{left:325px;top:202px;width:277px;height:28px;font-family:"Baloo 2",sans-serif;font-weight:700;font-size:15px;line-height:30px}
.intro{left:100px;top:235px;width:620px;text-align:center;font-size:15.5px;line-height:17.5px;color:var(--ink)}
.rv-frame{left:48px;top:334px;width:731px;height:94px;border:1.5px dotted var(--green-deep);border-radius:6px}
.rv-item{top:308px;width:70px;text-align:center}
.rv-ring{width:66px;height:66px;border-radius:50%;background:#fff;box-shadow:0 1px 4px rgba(0,0,0,.25);display:flex;align-items:center;justify-content:center;margin:0 auto}
.rv-label{font-size:13px;line-height:14px;margin-top:6px;color:var(--ink);font-weight:500}
.ewof-pill{left:228px;top:414px;width:338px;height:27px;font-size:13.5px;font-weight:500;line-height:29px;letter-spacing:.2px}
.service{left:46px;width:726px;height:120px}
.service .tile{left:0;top:0;width:128px;height:120px;border-radius:0 30px 0 0}
.service .curve{left:128px;top:95px;width:26px;height:25px}
.service .rule{left:0;bottom:0;width:726px;height:4px;border-radius:2px}
.service .title{left:151px;top:0;height:26px;border-radius:0 13px 13px 0;background:var(--green);color:#fff;font-family:"Baloo 2",sans-serif;font-weight:700;font-size:14px;line-height:28px;padding-left:12px}
.service .title::before{content:"";position:absolute;left:-5px;top:8px;width:9px;height:9px;border-radius:50%;background:var(--green);border:2px solid #fff}
.service .copy{left:154px;top:34px;width:560px;font-size:15px;line-height:16.5px;color:var(--ink)}
.grey .tile,.grey .rule{background:var(--grey)}
.lime .tile,.lime .rule{background:var(--green)}
.tile svg{position:absolute;left:28px;top:26px}
.general{left:49px;top:904px;width:730px;height:128px;background:linear-gradient(90deg,#1e6a3b,#213346);border-radius:0 8px 0 0}
.tab-green{left:49px;top:884px;width:214px;height:26px;background:var(--green);color:#fff;font-family:"Baloo 2",sans-serif;font-weight:700;font-size:14px;line-height:28px;padding-left:18px}
.tab-dark{left:263px;top:884px;width:247px;height:26px;background:#1e4f3c;color:#fff;font-family:"Baloo 2",sans-serif;font-weight:700;font-size:17px;line-height:28px;padding-left:18px}
.gen-item{top:940px;display:flex;align-items:center;gap:12px;color:#fff;font-size:19px;line-height:20px}
.gen-ring{width:54px;height:54px;border-radius:50%;background:#fff;border:3px solid #2e7a47;display:flex;align-items:center;justify-content:center;flex:none}
.gen-sep{top:940px;height:52px;border-left:1.5px dashed #cfe3d4}
.tear-band{left:49px;top:1010px;width:730px;height:90px;background:var(--mist)}
.person{left:49px;top:1032px;width:730px;text-align:center}
.person .name{font-family:"Baloo 2",sans-serif;font-weight:700;color:var(--green);font-size:20px;line-height:22px}
.person .role{font-family:"Baloo 2",sans-serif;font-weight:700;color:#111;font-size:20px;line-height:22px}
.footer{left:0;top:1095px;width:820px;height:65px;background:var(--teal-dark)}
.contact{top:1115px;display:flex;align-items:center;gap:7px;color:#fff;font-size:17px;font-weight:500}
.contact-sep{top:1112px;height:30px;border-left:1.5px dashed #cfd8d4}
.stamp{left:636px;top:1064px;width:184px;height:96px;background:#fff;border-radius:20px 0 0 0;border-top:6px solid var(--green);border-left:6px solid var(--green)}
.stamp-name{left:660px;top:1097px;font-family:"Hind",sans-serif;font-weight:600;font-size:26px;color:var(--green-deep);line-height:1}
.stamp-square{left:790px;top:1103px;width:12px;height:12px;background:var(--green)}
</style>
</head>
<body>
<div class="flyer">

  <svg class="abs header" viewBox="0 0 820 270" aria-hidden="true">
    <defs>
      <linearGradient id="headGrad" x1="0" x2="1" y1="0" y2="0">
        <stop offset="0" stop-color="#17703a"/>
        <stop offset="1" stop-color="#22334a"/>
      </linearGradient>
    </defs>
    <path fill="url(#headGrad)" d="M0 0H820V160L805 166 790 158 770 170 748 162 725 174 700 168 680 178 655 170 630 180 600 172 575 182 550 176 520 186 495 178 470 184 440 176 415 186 390 176 360 182 335 172 310 180 285 168 260 176 238 168 215 172 190 160 170 168 148 155 125 166 100 154 80 162 58 152 40 158 20 150 0 156Z"/>
  </svg>
  <div class="abs brand">Voltarey</div>
  <div class="abs tagline">New builds, Renovations, Maintenance and more!</div>
  <div class="abs portrait" role="img" aria-label="Photo of an electrician in a hard hat and safety glasses working at a switchboard"></div>

  <div class="abs dotline" style="left:52px;top:215px;width:714px"></div>
  <div class="abs dot" style="left:48px;top:211px"></div>
  <div class="abs dot" style="left:762px;top:211px"></div>
  <div class="abs pill-dark section-pill">Motorhome and Caravan EWOFs</div>
  <p class="abs intro">Recreational Vehicles (such as caravans, motorhomes, RVs, Boats etc) and Relocatable buildings that can be connected to an electricity supply must be regularly checked for electrical safety.</p>

  <div class="abs rv-frame"></div>
  <div class="abs rv-item" style="left:215px">
    <div class="rv-ring"><svg width="44" height="30" viewBox="0 0 44 30" fill="none" stroke="#1d3a3a" stroke-width="1.8"><rect x="6" y="4" width="32" height="18" rx="4"/><rect x="11" y="8" width="10" height="6"/><rect x="26" y="8" width="6" height="12"/><circle cx="18" cy="24" r="3.5"/><path d="M2 22H6M38 20H43"/></svg></div>
    <div class="rv-label">Caravans</div>
  </div>
  <div class="abs rv-item" style="left:293px">
    <div class="rv-ring"><svg width="44" height="32" viewBox="0 0 44 32" fill="none" stroke="#1d3a3a" stroke-width="1.8"><path d="M3 24V6H32L40 16V24Z"/><rect x="8" y="10" width="10" height="6"/><rect x="22" y="10" width="7" height="12"/><circle cx="11" cy="26" r="3.5"/><circle cx="33" cy="26" r="3.5"/></svg></div>
    <div class="rv-label">Motorhomes</div>
  </div>
  <div class="abs rv-item" style="left:373px">
    <div class="rv-ring"><svg width="44" height="32" viewBox="0 0 44 32" fill="none" stroke="#1d3a3a" stroke-width="1.8"><path d="M3 24V4H34V12H41V24Z"/><rect x="8" y="8" width="10" height="7"/><rect x="22" y="12" width="7" height="10"/><circle cx="11" cy="26" r="3.5"/><circle cx="34" cy="26" r="3.5"/></svg></div>
    <div class="rv-label">RVs</div>
  </div>
  <div class="abs rv-item" style="left:450px">
    <div class="rv-ring"><svg width="44" height="30" viewBox="0 0 44 30" fill="none" stroke="#1d3a3a" stroke-width="1.8"><path d="M2 18H42L36 26H8Z"/><path d="M10 18V12H28L34 18"/><path d="M16 12V7H24V12"/><path d="M2 28H42"/></svg></div>
    <div class="rv-label">Boats</div>
  </div>
  <div class="abs rv-item" style="left:528px">
    <div class="rv-ring"><svg width="36" height="36" viewBox="0 0 36 36" fill="none" stroke="#1d3a3a" stroke-width="1.8"><rect x="5" y="8" width="26" height="24"/><rect x="10" y="3" width="16" height="5"/><path d="M10 13H14M16 13H20M22 13H26M10 19H14M16 19H20M22 19H26M15 32V25H21V32"/></svg></div>
    <div class="rv-label">Relocatable buildings</div>
  </div>
  <div class="abs pill-dark ewof-pill">AN EWOF NEEDS TO BE ISSUED EVERY 4 YEARS</div>

  <section class="abs service grey" style="top:469px">
    <div class="abs tile"><svg width="70" height="66" viewBox="0 0 70 66" fill="none" stroke="#fff" stroke-width="2"><path d="M4 64V34L18 24 32 34V64Z"/><path d="M12 64V48H24V64"/><rect x="16" y="6" width="36" height="22"/><rect x="34" y="22" width="24" height="32" rx="2"/><path d="M39 30H52M39 37H52M39 44H47"/><circle cx="53" cy="50" r="6"/><path d="M57 54L64 61"/></svg></div>
    <svg class="abs curve" viewBox="0 0 26 25"><path d="M0 0V25H26C10 25 0 16 0 0Z" fill="#676767"/></svg>
    <div class="abs rule"></div>
    <div class="abs title" style="width:237px">Pre-purchase house inspections</div>
    <p class="abs copy">A pre-purchase electrical inspection prior to buying a home can be used to identify any dangerous and unsafe electrical parts of the installation that may be costly to repair once the property has been purchased. Giving you peace of mind when buying your new home.</p>
  </section>

  <section class="abs service lime" style="top:609px">
    <div class="abs tile"><svg width="70" height="70" viewBox="0 0 70 70" fill="none" stroke="#fff" stroke-width="2"><path d="M10 20A12 12 0 0 1 34 20H8"/><circle cx="21" cy="28" r="7"/><path d="M6 64V48Q6 40 14 40H28"/><rect x="30" y="36" width="18" height="30" rx="3"/><rect x="34" y="40" width="10" height="8"/><circle cx="39" cy="56" r="4"/><circle cx="46" cy="14" r="6"/><path d="M44 22H48M46 2V4M55 7L53 9M37 7L39 9"/></svg></div>
    <svg class="abs curve" viewBox="0 0 26 25"><path d="M0 0V25H26C10 25 0 16 0 0Z" fill="#56b148"/></svg>
    <div class="abs rule"></div>
    <div class="abs title" style="width:260px">High risk Electrical inspections</div>
    <p class="abs copy">All Prescribed Electrical Work that falls under the High Risk category must be inspected by a Registered Electrical Inspector and have a Record of Inspection certificate issued.</p>
  </section>

  <section class="abs service grey" style="top:750px">
    <div class="abs tile"><svg width="80" height="68" viewBox="0 0 80 68" fill="none" stroke="#fff" stroke-width="2"><rect x="2" y="2" width="22" height="62" rx="4"/><circle cx="13" cy="14" r="6"/><path d="M14 10L11 14H15L12 18"/><path d="M24 36H30V30"/><path d="M20 50H74V60H20Z"/><path d="M28 50L36 38H60L70 50"/><circle cx="32" cy="60" r="5"/><circle cx="64" cy="60" r="5"/></svg></div>
    <svg class="abs curve" viewBox="0 0 26 25"><path d="M0 0V25H26C10 25 0 16 0 0Z" fill="#676767"/></svg>
    <div class="abs rule"></div>
    <div class="abs title" style="width:260px">Electric Vehicle Chargers</div>
    <p class="abs copy" style="width:490px">Any electrical vehicle charger that can be accessed by the public (ie in a non-domestic situation) must be periodically inspected and certified every 12 months.</p>
  </section>

  <div class="abs general"></div>
  <div class="abs tab-green">General Electrical Services</div>
  <div class="abs tab-dark">Domestic and commercial</div>
  <div class="abs gen-item" style="left:80px">
    <div class="gen-ring"><svg width="28" height="28" viewBox="0 0 28 28" fill="none" stroke="#1d3a3a" stroke-width="1.6"><rect x="4" y="6" width="20" height="20"/><rect x="8" y="2" width="12" height="4"/><path d="M8 11H11M13 11H16M18 11H21M8 16H11M13 16H16M18 16H21M12 26V21H16V26"/></svg></div>
    <span>We do new<br>builds</span>
  </div>
  <div class="abs gen-sep" style="left:290px"></div>
  <div class="abs gen-item" style="left:298px">
    <div class="gen-ring"><svg width="28" height="28" viewBox="0 0 28 28" fill="none" stroke="#1d3a3a" stroke-width="1.6"><path d="M3 13L14 3 25 13M6 11V25H22V11"/><path d="M11 22L19 14 21 16 13 24H11Z"/></svg></div>
    <span>Renovations</span>
  </div>
  <div class="abs gen-sep" style="left:514px"></div>
  <div class="abs gen-item" style="left:520px">
    <div class="gen-ring"><svg width="28" height="28" viewBox="0 0 28 28" fill="none" stroke="#1d3a3a" stroke-width="1.6"><circle cx="14" cy="14" r="11" stroke-dasharray="3 2"/><circle cx="14" cy="14" r="6"/><path d="M14 10V14M11.5 11.5A4 4 0 1 0 16.5 11.5"/></svg></div>
    <span>Maintenance and<br>more!</span>
  </div>

  <svg class="abs tear-band" viewBox="0 0 730 90" preserveAspectRatio="none" aria-hidden="true" style="background:none">
    <path fill="#e2e3e5" d="M0 12L20 6 45 14 70 4 95 12 120 2 150 10 175 0 200 8 230 4 255 14 280 6 310 12 340 2 365 10 395 4 420 14 450 6 480 12 505 2 535 10 560 4 590 12 615 6 645 14 670 4 700 10 730 6V90H0Z"/>
  </svg>
  <div class="abs person">
    <div class="name">DEAN FOWLER</div>
    <div class="role">Electrician and Electrical Inspector</div>
  </div>

  <div class="abs footer"></div>
  <div class="abs contact" style="left:45px">
    <svg width="22" height="18" viewBox="0 0 22 18" fill="none" stroke="#56b148" stroke-width="2"><rect x="1" y="1" width="20" height="16" rx="2"/><path d="M1 2L11 10 21 2"/></svg>
    <span>Dean@voltarey.co.nz</span>
  </div>
  <div class="abs contact-sep" style="left:344px"></div>
  <div class="abs contact" style="left:358px">
    <svg width="22" height="20" viewBox="0 0 22 20" fill="#56b148"><path d="M1 7Q11 -1 21 7L18 10 15 8V6Q11 4 7 6V8L4 10Z"/><path d="M5 11H17L19 19H3Z"/></svg>
    <span>0227839152</span>
  </div>
  <div class="abs contact-sep" style="left:504px"></div>
  <div class="abs contact" style="left:516px">
    <svg width="18" height="24" viewBox="0 0 18 24" fill="#56b148"><path d="M9 0A9 9 0 0 0 0 9C0 15 9 24 9 24S18 15 18 9A9 9 0 0 0 9 0ZM9 13A4 4 0 1 1 9 5 4 4 0 0 1 9 13Z"/></svg>
    <span>Auckland</span>
  </div>

  <div class="abs stamp"></div>
  <div class="abs stamp-name">Voltarey</div>
  <div class="abs stamp-square"></div>

</div>
</body>
</html>
```